Tidewind Coves Boat Business Website

I would like a website that looks fresh, fun and exciting with great colors and photos of people having fun sailing and power boating. Current web page is www.tidewindcoves.example. I want to be able to change content and photos myself once completed. Also needs to have customized info request forms and access to enrollment forms. Should work across all browsers and platforms including iPad and Mac. I have three product lines...instruction, charters and trips. See also keelhour.example/new-york, and facebook.com/tidewindcoves, /keelhournewyork and /coralpalmlounge.

Reason: We are reviewing the designs submitted and will provide feedback asap. Thank you.

Industry/Entity Type

Business

Requirements
Must have
• self management/content management
form submissions
color, fun, excitement
links pages
photo pages
Nice to have
• calendar/class scheduling
guest book
visitor uploadable photos

```html
<!DOCTYPE html>
<html lang="en">
<head>
<meta charset="utf-8">
<title>Tidewind Coves – We Set Sailing!</title>
<link rel="stylesheet" href="https://fonts.googleapis.com/css2?family=Ubuntu:wght@400;500;700&family=Gilda+Display&display=swap">
<style>
  :root {
    --nav-bg: #b9dde8;
    --nav-active: #cfe8f0;
    --nav-divider: #d8edf3;
    --nav-text: #2a93b8;
    --nav-text-active: #1a6f93;
    --hero-top: #3aa8cf;
    --hero-bottom: #1f8cb8;
    --hero-edge: #167aa3;
    --page-bg: #f7f7f7;
    --white: #ffffff;
    --frame: #f1f1f1;
    --photo-top: #4a5660;
    --photo-bottom: #2c3a4a;
    --dot-panel: rgba(20, 28, 36, 0.85);
    --dot: #e6e6e6;
    --dot-active: #1a86c0;
    --btn-top: #3ab0dd;
    --btn-bottom: #0b6d9e;
    --heading: #2b2b2b;
    --body-text: #777777;
    --rule: #e2e2e2;
  }
  * { box-sizing: border-box; margin: 0; padding: 0; }
  html, body {
    width: 1200px; height: 703px; overflow: hidden;
    background: var(--white);
  }
  .page {
    position: relative; width: 1200px; height: 703px;
    background: var(--page-bg); overflow: hidden;
    font-family: Arial, Helvetica, sans-serif;
  }
  .main-nav {
    position: absolute; left: 0; top: 0; width: 1178px; height: 62px;
    background: var(--nav-bg); display: flex;
    border-bottom: 1px solid #a9d2df;
  }
  .main-nav a {
    display: flex; align-items: center; justify-content: center;
    height: 100%; text-decoration: none;
    font-family: "Ubuntu", sans-serif; font-weight: 500; font-size: 19px;
    color: var(--nav-text); border-right: 2px solid var(--nav-divider);
  }
  .main-nav a.is-active { background: var(--nav-active); color: var(--nav-text-active); margin-left: 18px; }
  .hero {
    position: absolute; left: 0; top: 62px; width: 1178px; height: 334px;
    background: linear-gradient(180deg, var(--hero-top), var(--hero-bottom));
    border-bottom: 2px solid var(--hero-edge);
  }
  .hero-title {
    position: absolute; left: 69px; top: 62px;
    font-family: "Gilda Display", serif; font-weight: 400; font-size: 33px; line-height: 42px;
    color: var(--white); text-shadow: 2px 3px 5px rgba(0,0,0,0.55);
  }
  .hero-title span { display: block; }
  .hero-title .tagline { padding-left: 42px; }
  .hero-intro {
    position: absolute; left: 17px; top: 192px; width: 500px;
    font-size: 14px; line-height: 26px; color: var(--white);
  }
  .cta-button {
    position: absolute; left: 18px; top: 414px; width: 226px; height: 49px;
    border-radius: 5px; border: 1px solid #0a5f8a;
    background: linear-gradient(180deg, var(--btn-top), var(--btn-bottom));
    box-shadow: 0 8px 10px -6px rgba(0,0,0,0.35);
    display: flex; align-items: center; justify-content: center;
    font-family: "Ubuntu", sans-serif; font-weight: 700; font-size: 18px; color: var(--white);
    text-decoration: none;
  }
  .slider-frame {
    position: absolute; left: 537px; top: 94px; width: 617px; height: 375px;
    background: var(--frame); border-radius: 3px;
    box-shadow: 0 10px 14px -8px rgba(0,0,0,0.35);
  }
  .slide-photo {
    position: absolute; left: 18px; top: 17px; width: 582px; height: 338px;
    background: linear-gradient(180deg, var(--photo-top) 0%, var(--photo-bottom) 70%, #3b4d63 100%);
  }
  .slide-dots {
    position: absolute; right: 0; bottom: 0; width: 161px; height: 42px;
    background: var(--dot-panel); display: flex; align-items: center; justify-content: center; gap: 12px;
  }
  .slide-dots i { width: 19px; height: 19px; border-radius: 50%; background: var(--dot); display: block; }
  .slide-dots i.is-current { background: var(--dot-active); box-shadow: inset 0 0 0 2px #0d5f8c; }
  .intro-heading {
    position: absolute; left: 0; top: 518px; width: 1178px; text-align: center;
    font-family: "Ubuntu", sans-serif; font-weight: 500; font-size: 31px; color: var(--heading);
  }
  .intro-quote {
    position: absolute; left: 128px; top: 575px; width: 936px; text-align: center;
    font-size: 14px; line-height: 26px; color: var(--body-text);
  }
  .intro-quote .mark { font-family: Georgia, serif; font-size: 22px; color: #9a9a9a; vertical-align: -4px; margin-right: 4px; }
  .section-rule {
    position: absolute; left: 30px; top: 670px; width: 1130px; height: 2px; background: var(--rule);
  }
</style>
</head>
<body>
<div class="page">
  <nav class="main-nav">
    <a class="is-active" href="#" style="width:136px">HOME</a>
    <a href="#" style="width:168px">SERVICES</a>
    <a href="#" style="width:170px">CAPTAINS</a>
    <a href="#" style="width:150px">TRAVEL</a>
    <a href="#" style="width:157px">SIGN UP!</a>
    <a href="#" style="width:159px">SITEMAP</a>
    <a href="#" style="width:168px">CONTACT</a>
  </nav>

  <header class="hero">
    <h1 class="hero-title">
      <span>TidewindCoves</span>
      <span class="tagline">We Set Sailing!</span>
    </h1>
    <p class="hero-intro">Lorem ipsum dolor sit amet, consectetur adipiscing elit. Aenean quam ante, egestas tristique consequat ut, pulvinar a ante. Donec commodo eros at felis tempor at porttitor mauris adipisci morbi in velit sapien modo eros at felis te adispicing ulvinar a ante donec commodo eros at felis.</p>
  </header>

  <div class="slider-frame">
    <div class="slide-photo" role="img" aria-label="Sailboat with crew heeling hard under a billowing white sail on rough grey sea"></div>
    <div class="slide-dots" style="right:17px;bottom:20px">
      <i></i><i class="is-current"></i><i></i><i></i><i></i>
    </div>
  </div>

  <a class="cta-button" href="#">Set Sailing Now!</a>

  <h2 class="intro-heading">Set Sailing With Tidewind Coves!</h2>
  <p class="intro-quote"><span class="mark">&ldquo;</span>Lorem ipsum dolor sit amet, consectetur adipiscing elit. Cras molestie condimentum consequat. Nam leo libero, scelerisque tincidunt commodo id, hendrerit vitae orci. Suspendisse eget nibh turpis. Sed at accumsan neque. Praesent purus eros, egestas eu tempus ut, mollis et libero&rdquo;</p>
  <div class="section-rule"></div>
</div>
</body>
</html>
```